Restaurant needs promotional material

We need a design for a "free welcome cocktail on your next visit" flyer. The flyer must have a black background and be contemporary. Our logo is the name of the restaurant which is "Ember Nook" in edwardian script font with italic selected.

There must be a section for terms and conditions, which are:
1 free cocktail for every main course ordered from our evening menu over the value of 9.95€ (not including taxes). The number of free cocktails cannot exceed the number of main courses ordered from your previous visit. This offer is only valid when you present both this flyer and your receipt from your previous visit. This offer does not include ice cream cocktails. This offer cannot be used in conjunction with any other offer or promotion. Limit 1 free cocktail per person. We reserve the right to final interpretation of this offer and can cancel the offer at any time.

A space must also be left where we can write a "valid until" date.

The uploaded photos are a picture of our cocktail menu and the publicity we are currently running, so you can get a feel for your design.

Thanks

Industry/Entity Type

Restaurant

Colors
000000

Requirements
Must have
• Also included in the flyer is the text " Please present this flyer along with your bill from your previous visit upon arrival.
• Pictures of cocktails!

```html
<!DOCTYPE html>
<html lang="en">
<head>
<meta charset="utf-8">
<title>Ember Nook – Free Welcome Cocktail Flyer</title>
<link rel="stylesheet" href="https://fonts.googleapis.com/css2?family=Josefin+Sans:wght@700&family=Open+Sans:wdth,wght@75,300;75,600;100,300&display=swap">
<style>
  :root {
    --ink: #1b1c1e;
    --ink-deep: #0e0f10;
    --pink: #e3268f;
    --pink-dark: #a8125f;
    --pink-soft: #e04a9f;
    --paper: #ffffff;
    --page: #e9e9e9;
  }
  * { margin: 0; padding: 0; box-sizing: border-box; }
  html, body { width: 877px; height: 1200px; overflow: hidden; background: var(--page); }
  .flyer {
    position: relative;
    width: 877px;
    height: 1200px;
    overflow: hidden;
    background:
      linear-gradient(160deg, rgba(255,255,255,0.06) 0%, rgba(255,255,255,0) 35%),
      repeating-linear-gradient(-18deg, rgba(255,255,255,0.025) 0 40px, rgba(255,255,255,0) 40px 110px),
      linear-gradient(180deg, #2a2c2f 0%, var(--ink) 35%, var(--ink-deep) 100%);
    font-family: "Open Sans", Arial, sans-serif;
    color: var(--paper);
  }
  .brand-ribbon {
    position: absolute;
    left: 61px; top: 0;
    width: 173px; height: 232px;
  }
  .brand-ribbon svg { position: absolute; inset: 0; }
  .brand-label {
    position: absolute; right: 14px; top: 38px;
    font-size: 14px; font-weight: 600; font-stretch: 75%;
    color: var(--paper);
  }
  .brand-name {
    position: absolute; left: 0; right: 0; top: 70px;
    text-align: center;
    font-size: 46px; line-height: 52px; font-weight: 300;
    color: var(--paper);
  }
  .valid-until {
    position: absolute; left: 563px; top: 36px;
    width: 216px; height: 94px;
  }
  .valid-until svg { position: absolute; inset: 0; }
  .valid-until span {
    position: absolute; left: 0; right: 0; top: 10px;
    text-align: center;
    font-family: "Josefin Sans", Arial, sans-serif;
    font-weight: 700; font-size: 21px; letter-spacing: 0.5px;
    color: var(--pink);
  }
  .headline {
    position: absolute; left: 0; right: 0; top: 200px;
    text-align: center;
    font-family: "Josefin Sans", Arial, sans-serif;
    font-weight: 700;
    color: var(--pink);
    -webkit-text-stroke: 1.5px var(--pink-dark);
    text-shadow: 0 0 14px rgba(227,38,143,0.45);
  }
  .headline-free { display: block; font-size: 132px; line-height: 132px; letter-spacing: 4px; }
  .headline-offer { display: block; font-size: 66px; line-height: 66px; margin-top: 6px; }
  .headline-visit { display: block; font-size: 58px; line-height: 64px; }
  .cocktail-photo {
    position: absolute; left: 420px; top: 530px;
    width: 457px; height: 670px;
    background:
      radial-gradient(ellipse 45% 30% at 68% 45%, rgba(240,170,230,0.85) 0%, rgba(205,90,190,0.55) 45%, rgba(120,30,110,0) 100%),
      radial-gradient(ellipse 22% 30% at 45% 22%, rgba(230,150,220,0.5) 0%, rgba(120,30,110,0) 100%),
      radial-gradient(ellipse 12% 10% at 72% 92%, rgba(240,160,230,0.7) 0%, rgba(120,30,110,0) 100%);
  }
  .terms { position: absolute; left: 36px; top: 494px; width: 400px; }
  .terms-title {
    font-size: 28px; font-weight: 300; font-stretch: 100%;
    color: var(--pink-soft); letter-spacing: 0.3px;
    margin-bottom: 14px;
  }
  .terms-list { list-style: none; }
  .terms-item {
    position: relative;
    padding-left: 33px;
    font-size: 17.5px; line-height: 25px;
    font-weight: 600; font-stretch: 75%;
    margin-bottom: 24px;
  }
  .terms-item.is-short { margin-bottom: 24px; }
  .terms-item::before {
    content: ""; position: absolute; left: 0; top: 1px;
    border-left: 14px solid var(--pink);
    border-top: 12px solid transparent;
    border-bottom: 12px solid transparent;
  }
  .arrival-note {
    position: absolute; left: 0; top: 1107px;
    width: 432px; height: 93px;
  }
  .arrival-note svg { position: absolute; inset: 0; }
  .arrival-note p {
    position: absolute; left: 35px; top: 14px;
    font-size: 21px; line-height: 25px;
    font-weight: 300; font-stretch: 75%;
    color: var(--paper);
  }
</style>
</head>
<body>
  <main class="flyer">
    <div class="brand-ribbon">
      <svg width="173" height="232" viewBox="0 0 173 232">
        <polygon points="0,0 173,0 173,232 86.5,212 0,232" fill="var(--pink)"/>
      </svg>
      <span class="brand-label">Restaurant</span>
      <div class="brand-name">Ember<br>Nook</div>
    </div>

    <div class="valid-until">
      <svg width="216" height="94" viewBox="0 0 216 94">
        <polygon points="0,0 216,0 216,72 108,94 0,72" fill="var(--paper)"/>
      </svg>
      <span>VALID UNTIL</span>
    </div>

    <h1 class="headline">
      <span class="headline-free">FREE</span>
      <span class="headline-offer">WELCOME COCKTAIL</span>
      <span class="headline-visit">ON YOUR NEXT VISIT</span>
    </h1>

    <div class="cocktail-photo" role="img" aria-label="Photo of a glowing pink cocktail in a martini glass with a lime wedge, splashing against the dark background"></div>

    <section class="terms">
      <h2 class="terms-title">TERMS AND CONDITIONS</h2>
      <ul class="terms-list">
        <li class="terms-item">1 free cocktail for every main course ordered from our evening menu over the value of 9.95€ (not including taxes).</li>
        <li class="terms-item">The number of free cocktails cannot exceed the number of main courses ordered from your previous visit.</li>
        <li class="terms-item">This offer is only valid when you present both this flyer and your receipt from your previous visit.</li>
        <li class="terms-item is-short">This offer does not include ice cream cocktails.</li>
        <li class="terms-item">This offer cannot be used in conjunction with any other offer or promotion. Limit 1 free cocktail per person.</li>
        <li class="terms-item">We reserve the right to final interpretation of this offer and can cancel the offer at any time.</li>
      </ul>
    </section>

    <div class="arrival-note">
      <svg width="432" height="93" viewBox="0 0 432 93">
        <polygon points="0,0 379,0 432,93 0,93" fill="var(--pink)"/>
      </svg>
      <p>Please present this flyer along with your bill<br>from your previous visit upon arrival</p>
    </div>
  </main>
</body>
</html>
```